11"x17" Poster for a Treasure Hunt

Summary:
This project is for a poster that will be used to promote a community treasure hunt for kids aged 9-14. This will be the 11th year we have run the treasure hunt. See the files for previous posters we have used (from ArtFolio).

Please thoroughly read below before embarking on this project.

We loved everything about the 2012 design, particularly how all of the elements seem to belong exactly where they are on the poster. Previous years designs just had text blocks thrown on top of a background image which doesn't make a for a good poster; if within a few seconds you don’t have an idea about what even the poster is promoting, and if you can’t read every part of the poster from 6 feet away, the poster isn't working.

Please make the Mill Ridge Quest Seekers logo a featured part of the design. See the 2012 poster winner where the logo was right at the top and very prominent.

This is the video promoting this year's event:
https://clipvault.example/Kx7PqR2mZtA

Style: Scary, but remember the event is for children 9-14years old. The title of the hunt this year is “Vault of the Restless”. Below the title, place the tagline "The Chilling Secret of Westbrook Middle Academy". The theme this year will be zombies. We do not want zombies that look too gruesome so I've attached a zombie example below. Remember, we want scary, but NOT gross and gruesome. Integrate the picture of Westbrook Middle Academy into the poster (picture attached below)
The time period is the mid 1982. Integrate the picture of Westbrook Middle Academy into the poster

Some of the poster submissions from previous years were way too gruesome with the “monster”. Do keep in mind this event is for children. For good examples, see "MRQS 2012 Winner" below (our favorite to date).

Target Market(s)

Children 9-14 years old.

Industry/Entity Type

Community

Requirements
Must have
• Must have the logos of Tim Marlow, Fairhaven Orthodontics, and Mill Ridge Quest Seekers.
Nice to have
• Take a look at the attached zombie picture. Its a good example of how it can be scary, but not too scary, and without the blood and gore.
Should not have
• No blood and gore

```html
<!DOCTYPE html>
<html lang="en">
<head>
<meta charset="utf-8">
<title>Vault of the Restless – Poster</title>
<link rel="stylesheet" href="https://fonts.googleapis.com/css2?family=Creepster&family=Oswald:wght@400;500;600&display=swap">
<style>
  :root {
    --page: #ffffff;
    --wine-light: #a24a63;
    --wine: #7b2c41;
    --wine-deep: #4a1424;
    --night: #0b0707;
    --yellow: #eac526;
    --orange: #ef5f2a;
    --cream: #f3eee6;
    --white: #ffffff;
    --moon: #e9e6e2;
  }
  * { margin: 0; padding: 0; box-sizing: border-box; }
  html, body { width: 1200px; height: 1200px; overflow: hidden; background: var(--page); }
  .poster {
    position: absolute; left: 242px; top: 46px; width: 716px; height: 1107px; overflow: hidden;
    background: radial-gradient(ellipse 75% 45% at 50% 42%, var(--wine-light), var(--wine) 55%, var(--wine-deep) 100%);
    font-family: "Oswald", "Arial Narrow", sans-serif; color: var(--white); text-align: center;
  }
  .moon-scene {
    position: absolute; left: -60px; top: -60px; width: 214px; height: 214px; border-radius: 50%;
    background: radial-gradient(circle at 55% 50%, var(--moon), #cfcac6 70%, #bdb7b3);
  }
  .campus-photo {
    position: absolute; left: 60px; top: 425px; width: 596px; height: 300px; border-radius: 50%;
    background: radial-gradient(ellipse at center, rgba(230,200,210,.35), rgba(230,200,210,0) 70%);
  }
  .graveyard-scene {
    position: absolute; left: 0; bottom: 0; width: 100%; height: 640px;
    background: linear-gradient(to bottom, rgba(11,7,7,0) 0%, rgba(40,12,18,.55) 30%, rgba(11,7,7,.92) 62%, var(--night) 80%);
  }
  .line { position: absolute; left: 0; width: 100%; }
  .brand {
    top: 94px; font-weight: 500; font-size: 40px; letter-spacing: 1px; color: var(--cream); text-transform: uppercase; line-height: 1;
  }
  .brand-rule { top: 148px; left: 165px; width: 386px; height: 1px; background: var(--cream); opacity: .8; }
  .title, .tagline, .site { font-family: "Creepster", "Impact", cursive; color: var(--yellow); text-transform: uppercase; text-shadow: 2px 3px 0 rgba(0,0,0,.45); }
  .title { top: 190px; font-size: 60px; line-height: 1; letter-spacing: 1px; }
  .tagline { top: 272px; font-size: 42px; line-height: 48px; }
  .date { top: 370px; font-size: 42px; font-weight: 600; text-shadow: 2px 2px 0 rgba(0,0,0,.35); }
  .copy { font-size: 24px; font-weight: 500; text-transform: uppercase; line-height: 33px; text-shadow: 1px 2px 2px rgba(0,0,0,.5); }
  .pitch { top: 468px; }
  .pitch .school { color: var(--yellow); }
  .prize { top: 560px; font-size: 56px; font-weight: 500; color: var(--orange); text-transform: uppercase; line-height: 1; text-shadow: 2px 2px 2px rgba(0,0,0,.4); }
  .divider { top: 643px; left: 88px; width: 540px; height: 2px; background: var(--white); }
  .details { top: 660px; line-height: 32px; }
  .limit { top: 740px; font-size: 20px; font-weight: 500; color: var(--yellow); text-transform: uppercase; }
  .credits { top: 990px; font-size: 15px; font-weight: 500; line-height: 20px; text-transform: uppercase; }
  .site { top: 1030px; font-size: 30px; letter-spacing: 1px; }
  .sponsor {
    position: absolute; bottom: 44px; font-weight: 500; font-size: 15px; line-height: 18px; text-transform: uppercase; color: var(--white);
    display: flex; flex-direction: column; align-items: center; gap: 6px;
  }
  .sponsor-mark { width: 30px; height: 30px; background: var(--orange); }
  .sponsor-left { left: 24px; width: 110px; }
  .sponsor-right { right: 14px; width: 130px; }
  .sponsor-right .sponsor-mark { background: var(--white); border-radius: 50%; }
</style>
</head>
<body>
<main class="poster">
  <div class="moon-scene" role="img" aria-label="Full moon with flying bats"></div>
  <div class="campus-photo" role="img" aria-label="Faded aerial photograph of Westbrook Middle Academy campus"></div>
  <div class="graveyard-scene" role="img" aria-label="Silhouetted graveyard with bare trees, tombstones and shambling zombies"></div>

  <div class="line brand">Mill Ridge Quest Seekers</div>
  <div class="line brand-rule"></div>

  <h1 class="line title">Vault of the Restless</h1>
  <p class="line tagline">The Chilling Secret of<br>Westbrook Middle Academy</p>
  <p class="line date">October 22nd, 2016</p>

  <p class="line copy pitch">Be the first team to unravel the mystery behind the<br><span class="school">Westbrook Middle Academy</span> closure and you will find a</p>
  <p class="line prize">Fantastic Treasure!</p>
  <div class="line divider"></div>

  <p class="line copy details">Youth ages 9-14 are eligible to participate<br>Team applications open September 1st and are due ASAP</p>
  <p class="line limit">Space is limited to the first 50 teams</p>

  <p class="line credits">Presented by Tim Marlow of Harbor Lane Realty and<br>Dr. Nina Ortez of Fairhaven Orthodontics</p>
  <p class="line site">www.mrquestseekers.example</p>

  <div class="sponsor sponsor-left"><span class="sponsor-mark"></span>Tim Marlow</div>
  <div class="sponsor sponsor-right"><span class="sponsor-mark"></span>Fairhaven Orthodontics</div>
</main>
</body>
</html>
```